The Fern Barrel Pub- restaurant menu, new launch

This is a new restaurant launching Summer 2017. Restaurant is a conversion of long standing small town existing family pizza/italian restaurant. new concept shifts concept to a family pub atmosphere featuring familiar appetizers, burgers, wood-fired pizza, and daily specials, draft beer, full- bar.

atmosphere is casual. want menu to reflect a more current "vibe" than the old place did. Not cold and modern, but retain the cozy familiar feel, without seeming dated and old fashioned.

4 panel menu; 8.5 X 11; 2-4 color
Updates

Project Deadline Extended
Reason: I am interested in seeing more designs. I will be providing feedback in the next few days on all designs submitted. I will also be increasing the budget.

Target Market(s)

Family-Oriented Pub, rural location Berkshire County, MA. Mostly Blue collar customer, value oriented

Industry/Entity Type

American Restaurant

Font styles to use
Sans Serif

Colors

Designer to choose colors to be used in the design.

Requirements
Must have
• Clear, uncluttered design, Highlighted items as specified in draft file (to come)
• ability to make changes daily as menu changes
• each panel separate sheet to slide into binder sleeve

```html
<!DOCTYPE html>
<html lang="en">
<head>
<meta charset="utf-8">
<title>The Fern Barrel Pub – Menu</title>
<link href="https://fonts.googleapis.com/css2?family=Oswald:wght@300;400;600;700&family=Roboto+Condensed:ital,wght@0,400;0,700;1,400&display=swap" rel="stylesheet">
<style>
:root{
  --board:#1c1c1c;
  --board-light:#2a2a2a;
  --chalk:#f1f1f1;
  --chalk-soft:#d6d6d6;
  --chalk-dim:#b5b5b5;
  --seam:#111;
}
*{box-sizing:border-box;margin:0;padding:0}
html,body{width:928px;height:1200px;overflow:hidden;background:var(--board)}
.menu{
  width:928px;height:1200px;display:grid;
  grid-template-columns:464px 464px;grid-template-rows:600px 600px;
}
.panel{
  position:relative;padding:8px 16px 0 10px;color:var(--chalk);
  background:radial-gradient(ellipse at 50% 40%,var(--board-light),var(--board) 75%);
  border-right:1px solid var(--seam);border-bottom:1px solid var(--seam);
  font-family:"Roboto Condensed",sans-serif;overflow:hidden;
}
.panel.right{padding:8px 14px 0 20px}
.brand{
  text-align:center;font-family:"Oswald",sans-serif;font-weight:700;
  font-size:34px;line-height:1.2;text-transform:uppercase;letter-spacing:1px;
  color:var(--chalk);margin-bottom:14px;
}
.row{display:flex;justify-content:space-between;align-items:baseline}
.name{font-family:"Oswald",sans-serif;font-weight:600;font-size:20px;line-height:1.1;text-transform:uppercase}
.price{font-family:"Oswald",sans-serif;font-weight:400;font-size:17px;white-space:nowrap}
.desc{font-size:10px;line-height:1.2;color:var(--chalk-soft);margin:2px 0 6px 14px;font-weight:700}
.list{font-size:10px;line-height:1.2;color:var(--chalk-soft);margin-left:30px;font-weight:700}
.sub{display:flex;justify-content:space-between;font-size:10px;line-height:1.25;color:var(--chalk-soft);font-weight:700;margin-left:30px}
.sub .p{font-size:8px}
.section{
  text-align:center;font-family:"Oswald",sans-serif;font-weight:600;font-style:italic;
  font-size:17px;letter-spacing:5px;text-transform:uppercase;margin:4px 0 6px;
}
.heading{text-align:center;font-family:"Oswald",sans-serif;font-weight:700;font-size:21px;line-height:1.15;text-transform:uppercase}
.heading.small{font-size:14px;letter-spacing:1px}
.intro{text-align:center;font-size:10px;line-height:1.2;color:var(--chalk-soft);font-weight:700;margin:2px 0 4px}
.tight .name{line-height:1}
.indent{margin-left:14px}
.group-label{font-size:10px;font-weight:700;color:var(--chalk-soft);margin-left:14px;line-height:1.3}
.gap{height:8px}
</style>
</head>
<body>
<main class="menu">

  <!-- Starters -->
  <section class="panel left">
    <h1 class="brand">The Fern Barrel Pub</h1>
    <div class="row"><span class="name">Wings</span><span class="price">12,00 $</span></div>
    <p class="desc">A Baker's Ten (that's 11) of the biggest tastiest wings you'll find anywhere. Choose from our award winning sauces:</p>
    <p class="list" style="margin-top:-5px;margin-bottom:6px">Buffalo mild<br>Buffalo hot<br>Maple's Honey Chipotle<br>Garlic Parm<br>BBQ<br>Xtra Hot<br>Challenge Hot</p>
    <div class="row"><span class="name">Boneless “Wings”</span><span class="price">12,00 $</span></div>
    <p class="desc">Why are they called wings? They're not wings. But it's tasty boneless breaded chicken anyway. Same great sauces, 8 “Wings.”</p>
    <div class="row"><span class="name">‘Chos!!</span><span class="price">11,00 $</span></div>
    <p class="desc" style="margin-bottom:1px">Totchos and Nachos and Cheese, oh my!</p>
    <div class="sub"><span>Add brisket</span><span class="p">3,00 $</span></div>
    <div class="sub"><span>Add pulled pork</span><span class="p">3,00 $</span></div>
    <div class="sub" style="margin-bottom:6px"><span>Add chili</span><span class="p">3,00 $</span></div>
    <div class="row"><span class="name">Spinach Artichoke Dip</span><span class="price">10,00 $</span></div>
    <p class="desc">The good stuff. Real Spinach. Real Artichokes. Real Cheese. This did not come from a bag. We make it right here, every day.</p>
    <h2 class="section">Soups &amp; Stuff</h2>
    <div class="tight">
      <div class="row"><span class="name">Chowder</span><span class="price">6,00 $</span></div>
      <div class="row"><span class="name">Chili</span><span class="price">6,00 $</span></div>
      <div class="row"><span class="name">Du Jour</span><span class="price">6,00 $</span></div>
    </div>
    <h2 class="section" style="margin-top:10px">Salads</h2>
    <div class="tight">
      <div class="row"><span class="name">Fern Barrel Chopped Salad</span><span class="price">12,00 $</span></div>
      <div class="row"><span class="name">Gorgonzola Salad</span><span class="price">12,00 $</span></div>
    </div>
    <div class="sub" style="margin-left:14px;margin-top:3px"><span>Add chicken</span><span class="p">2,00 $</span></div>
  </section>

  <!-- Pizza -->
  <section class="panel right">
    <h1 class="brand">The Fern Barrel Pub</h1>
    <h2 class="heading">Wood Fired Pizza</h2>
    <p class="intro">All our dough is made fresh daily in house with just four ingredients: water, flour, salt and yeast. Baked to perfection in the wood over, Fern Barrel Pizza is the best in the county!</p>
    <h2 class="heading">Our Specialty Pies</h2>
    <div class="tight" style="margin-top:6px">
      <div class="row"><span class="name">Small</span><span class="price">13,00 $</span></div>
      <div class="row"><span class="name">Large</span><span class="price">17,00 $</span></div>
    </div>
    <p class="intro">The Buffalo Bird- buffalo sauce, grilled chicken, mozzarella and topped with red onion for just the right finish. Don't like onion? We'll leave it off!</p>
    <p class="intro">Chicken 'Q- house made BBQ sauce from Big Oak BBQ. Grilled chicken and mozzarella make this crowd favorite.</p>
    <p class="intro">The Hula Hule- Sliced ham and Pineapple, and mozzarella. It doesn't get any better! Ask for coconut, if you're feeling crazy!</p>
    <h2 class="heading">Create Your Own!</h2>
    <div class="tight" style="margin-top:6px">
      <div class="row"><span class="name">Small</span><span class="price">11,00 $</span></div>
      <div class="row"><span class="name">Large</span><span class="price">10,00 $</span></div>
    </div>
    <div class="sub" style="margin-left:14px;margin-top:4px"><span>Choose from standard toppings :</span><span class="p">2,00 $</span></div>
    <p class="list">Pepperoni, Onion, Tomato, Garlic, Green Pepper, Mushroom,<br>Sliced or Chopped Tomato, Broccoli, Spinach, Sliced black olives</p>
    <div class="sub" style="margin-left:14px"><span>More Meats:</span><span class="p">2,50 $</span></div>
    <p class="list">Meatball, Bacon, Sausage, Chicken, Ham</p>
    <div class="sub" style="margin-left:14px"><span>Specialty Toppings:</span><span class="p">3,00 $</span></div>
    <p class="list">Xtra Cheese, Pineapple, Feta, Ricotta, Kalamata Olives, Hot Peppers, Coconut, Artichokes, Sun dried Tomato, Pesto</p>
    <div class="sub" style="margin-left:14px"><span>Gluten Free add<br>(only small size)</span><span class="p">2,00 $</span></div>
    <h2 class="heading" style="font-style:italic;font-size:19px;margin-top:4px">Fold It Up!</h2>
    <p class="intro">Turn your Pizza into a calzone, specialty or build your own. Same price as a small.</p>
  </section>

  <!-- Burgers -->
  <section class="panel left">
    <h1 class="brand" style="margin-bottom:40px">The Fern Barrel Pub</h1>
    <h2 class="heading">Barrel Burgers</h2>
    <p class="intro">Our ground beef is pure 80/20 goodness, from Northeast farms, always fresh, hand packed daily for exceptional beef burger taste. Accept no substitutes- these are the best burgers anywhere.</p>
    <div class="row" style="margin-top:4px"><span class="name">The Barrel Burger “Original”</span><span class="price">10,99 $</span></div>
    <p class="desc">Double ¼ lb hand packed patties, with double American cheese, and double the Green Ridge Smokehouse Applewood Bacon. This beauty is served with Lettuce, Tomato, Onion, our world-class hand-cut fries, and a side of Barrel Sauce.</p>
    <h2 class="heading" style="margin-top:4px">Want to do it your way?<br>Over 100 possibilities!</h2>
    <div class="gap"></div><div class="gap"></div>
    <div class="sub" style="margin-left:14px;margin-right:70px"><span>¼ lb patty</span><span class="p">6,00 $</span></div>
    <div class="sub" style="margin-left:14px;margin-right:70px"><span>Double ¼</span><span class="p">8,00 $</span></div>
    <div class="sub" style="margin-left:14px;margin-right:70px"><span>Triple ¼</span><span class="p">9,00 $</span></div>
    <div class="sub" style="margin-left:14px;margin-right:70px"><span>Quad quarter</span><span class="p">10,00 $</span></div>
    <div class="gap"></div>
    <div class="sub" style="margin-left:14px;margin-right:70px"><span>1/3 lb patty</span><span class="p">8,00 $</span></div>
    <div class="sub" style="margin-left:14px;margin-right:70px"><span>Double 1/3</span><span class="p">11,00 $</span></div>
    <div class="sub" style="margin-left:14px;margin-right:70px"><span>Triple 1/3</span><span class="p">13,00 $</span></div>
    <div class="sub" style="margin-left:14px;margin-right:70px"><span>Quad 1/3</span><span class="p">15,00 $</span></div>
    <p class="group-label" style="margin-left:4px;margin-top:4px">ADD-ONS</p>
    <div class="sub" style="margin-left:14px"><span>Lettuce, Tomato, Onion, Pickle- no charge<br>Sliced Cheese- American, Cheddar, Swiss<br>Gorgonzola</span><span class="p">0,75 $<br>1,00 $</span></div>
    <div class="sub" style="margin-left:14px;margin-top:4px"><span>Green Ridge Smokehouse Applewood Bacon</span><span class="p">1,00 $</span></div>
    <div class="sub" style="margin-left:14px;margin-top:4px"><span>World-Class Hand-cut Fries</span><span class="p">2,50 $</span></div>
  </section>

  <!-- Specials -->
  <section class="panel right">
    <h1 class="brand" style="margin-bottom:40px">The Fern Barrel Pub</h1>
    <h2 class="heading">Daily Specials</h2>
    <h3 class="heading small">Where the craziness happens</h3>
    <div class="row" style="margin-top:4px"><span class="name">20 Layer Lasagna</span><span class="price">12,99 $</span></div>
    <p class="desc">Our signature dish sells out every week, get it when you can!</p>
    <div class="row"><span class="name">The Pig Pile</span><span class="price">11,00 $</span></div>
    <p class="desc">Our World-class Hand-cut fries topped with Pulled pork, Mozzarella, Crispy Bacon, BBQ sauce, and Topped with house onion rings. Not for the faint of heart, if you know what we mean...</p>
    <div class="row"><span class="name">Pasta Primavera</span><span class="price">12,99 $</span></div>
    <p class="desc">Fresh veggies, tossed with penne, in a garlic white wine butter sauce.</p>
    <div class="row"><span class="name">Chicken Parmesan</span><span class="price">15,00 $</span></div>
    <p class="desc">Two breaded chicken breasts topped with house marinara and mozzarella, served with penne marinara. Yum!</p>
    <div class="row"><span class="name">Pasta Carbonara</span><span class="price">15,00 $</span></div>
    <p class="desc">The creamy bacon pasta classic. You know it, you love it. Just say yes.</p>
    <div class="row"><span class="name">Buffalo Chicken Mac and Cheese</span><span class="price">13,00 $</span></div>
    <p class="desc">All the food groups in this one!<br>Chicken, Buffalo sauce, Mac and Cheese. A true food pyramid!</p>
  </section>

</main>
</body>
</html>
```